House-share and Room Rental Website (With Focus on the Bedroom Landing Page)

Looking for website design for our House-share (executive accommodation) and room rental business.

Our company name is: Quellnest could also be written as QuellNest or quellnest. Either is fine .. just looking for a nice clean catchy logo to go with the design.

EXAMPLES
These are examples of other websites in this field that are doing well. this is a kind of baseline.
https://dovelinter.example.au/
https://www.kestrib.example/
https://www.velunor.example/
https://www.trisbel.example/
https://www.pondmarrowseek.example.au/

Our business model is to rent rooms to people looking for high-quality accommodation. We fill the gap between those looking to rent rooms and those with rooms to rent. However, our model is slightly different from those already on the market as we looking to fill a massive gap in the market delivering upmarket rooms for rent.(Executive Accommodation) also in the back end will be coupled with a self management process in the back end.

We offer executive style accommodation that stands out above the rest. With special extras like fire safety.. and management processes that create happier homes. We are looking for a web design package that can help us grow and scale our business. We need a design that is captivating

Our MAIN focus is having a room landing page that stands out from the rest... The core of our business will rely on the promotion of the rooms in a share house... so the whole design relies on the BEDROOM landing page to drive results.

Target Market(s)

We have 2 markets we are aiming at ... the first market is people offering rooms to rent who want the highest rental return. The second market is people looking to rent safe, high-quality rooms, in houses that are well managed and looked after.

Industry/Entity Type

Share Economy

Logo Text

QuellNest

Number of Pages Required

5+ page

Font styles to use
Sans Serif

Colors
3276b5

Requirements
Must have
• A messaging system whereby we can create direct communication between those offering rooms and those looking for rooms.
• A call to action that says " Schedule an Inspection"
• Landing page for promoting rooms
• A home page for showing stock.
• Profile page for those selling rooms
• Profile page for those looking for rooms.
• A scheduling calendar for booking inspections
Nice to have
• Pages where new residents can lock in a room.. pay bond and rents.. and sign contracts
• Notifications
• SMS capabilities in the backend.
Should not have
• No script or handwriting fonts.

```html
<!DOCTYPE html>
<html lang="en">
<head>
<meta charset="utf-8">
<title>Quellnest – Executive Accommodation</title>
<link rel="stylesheet" href="https://fonts.googleapis.com/css2?family=Montserrat:wght@400;500;600;700;800&display=swap">
<style>
:root{
  --ink:#151617;
  --text:#2a2a2a;
  --muted:#666a6e;
  --field:#8a8d90;
  --line:#b9bcbf;
  --blue:#2190ec;
  --price:#1b84de;
  --amber:#e7a826;
  --band:#edf0f3;
  --white:#ffffff;
}
*{box-sizing:border-box;margin:0;padding:0}
html,body{width:822px;height:1200px;overflow:hidden}
body{position:relative;font-family:'Montserrat',sans-serif;color:var(--text);background:var(--white)}
.abs{position:absolute}

/* header */
.site-header{left:0;top:0;width:822px;height:37px;background:var(--ink)}
.brand{left:115px;top:5px;display:flex;align-items:center;gap:6px}
.brand-dot{width:26px;height:26px;border-radius:50%;background:var(--blue)}
.brand-name{font-size:17px;font-weight:500;color:var(--white);line-height:15px;letter-spacing:.3px}
.brand-tag{font-size:7px;color:var(--white);font-weight:400;line-height:9px;margin-top:2px}
.nav{top:14px;font-size:6.3px;font-weight:500;color:var(--white);white-space:nowrap}
.menu{left:690px;top:12px;width:15px}
.menu span{display:block;height:2.5px;background:var(--white);border-radius:1px;margin-bottom:3px}

/* hero */
.hero{left:0;top:37px;width:822px;height:357px;background:linear-gradient(180deg,#3d4a5c 0%,#56606a 38%,#6b5a4c 62%,#5f7a3c 84%,#7d9a4a 100%)}
.hero-title{left:0;top:117px;width:822px;text-align:center;font-size:19px;font-weight:800;line-height:25px;color:var(--white);letter-spacing:.8px}

/* search panel */
.tab{top:197px;height:49px;display:flex;align-items:center;justify-content:center;font-size:12.5px;font-weight:800;color:var(--white);letter-spacing:.3px}
.tab-search{left:126px;width:288px;background:var(--blue);padding-top:5px}
.tab-offer{left:414px;width:282px;background:var(--amber)}
.tab-pointer{left:128px;top:246px;width:0;height:0;border-left:7px solid transparent;border-right:7px solid transparent;border-top:9px solid var(--blue)}
.panel{left:126px;top:246px;width:570px;height:224px;background:var(--white);box-shadow:0 1px 4px rgba(0,0,0,.18)}
.label{font-size:7.5px;color:#333;font-weight:400}
.check{display:flex;align-items:center;gap:6px;font-size:9.5px;font-weight:700;color:var(--field)}
.box{width:11px;height:11px;border:1px solid var(--line);background:var(--white)}
.select{height:27px;width:129px;border:1px solid var(--line);display:flex;align-items:center;justify-content:space-between;padding:0 8px 0 7px;font-size:9.5px;font-weight:700;color:var(--field)}
.chev{width:5px;height:5px;border-right:1.2px solid #333;border-bottom:1.2px solid #333;transform:rotate(45deg);margin-top:-3px}
.submit{left:578px;top:418px;width:100px;height:27px;background:var(--ink);color:var(--white);font-size:9.5px;font-weight:700;display:flex;align-items:center;justify-content:center;border-radius:2px}

/* featured */
.section-title{font-size:15.5px;font-weight:500;color:var(--text)}
.city-pick{left:610px;top:520px;width:84px;height:18px;border:1px solid #999;font-size:7.5px;color:#555;display:flex;align-items:center;justify-content:space-between;padding:0 7px}
.city-pick .chev{width:4px;height:4px}
.room{top:562px;width:180px}
.room-photo{width:180px;height:125px}
.room-body{padding:13px 2px 0 2px}
.room-body h4{font-size:7.5px;font-weight:800;color:#222;line-height:9px}
.room-addr{font-size:7.5px;color:#555;margin:4px 0 7px;line-height:9px}
.room-price{font-size:7.5px;font-weight:700;color:var(--price);margin:6px 0 7px;line-height:9px}
.room-desc{font-size:7.5px;color:#555;line-height:12.5px;margin-top:4px;margin-left:-2px}
.room-go{width:12px;height:12px;background:var(--amber);display:flex;align-items:center;justify-content:center}
.room-go i{width:4px;height:4px;border-right:1.2px solid #fff;border-top:1.2px solid #fff;transform:rotate(45deg);margin-left:-2px}
.slide-btn{top:676px;width:25px;height:24px;background:#dedfe0;display:flex;align-items:center;justify-content:center}
.slide-btn i{width:8px;height:8px;border-left:1.2px solid #fff;border-bottom:1.2px solid #fff}

/* how it works */
.how{left:0;top:882px;width:822px;height:240px;background:var(--band)}
.step{top:964px;width:180px;text-align:center}
.step-icon{margin:0 auto;width:60px;height:58px;border-radius:4px}
.step h3{font-size:11px;font-weight:500;color:var(--text);margin-top:15px}
.step p{font-size:7.5px;color:#666;line-height:12.5px;margin:10px auto 0;width:168px}

/* footer */
.site-footer{left:0;top:1122px;width:822px;height:38px;background:var(--ink)}
.foot-link{top:16px;font-size:6.5px;color:var(--white);font-weight:500}
.social{top:15px;display:flex;gap:7px}
.social span{width:9px;height:9px;border-radius:50%;background:var(--blue)}
.copyright{left:0;top:1175px;width:822px;text-align:center;font-size:6.5px;color:#333}
</style>
</head>
<body>

<header class="site-header abs">
  <div class="brand abs">
    <span class="brand-dot"></span>
    <div>
      <div class="brand-name">Quellnest</div>
      <div class="brand-tag">Executive Accommodation</div>
    </div>
  </div>
  <span class="nav abs" style="left:568px">CREATE AN ACCOUNT</span>
  <span class="nav abs" style="left:652px">LOGIN</span>
  <div class="menu abs"><span></span><span></span><span></span></div>
</header>

<section class="hero abs" role="img" aria-label="Photo of a brick family house with a grey roof, trees and a green lawn under a cloudy sky"></section>
<h1 class="hero-title abs">WELCOME TO THE EASIEST WAY TO<br>HOUSE-SHARE OR RENT A ROOM</h1>

<div class="tab tab-search abs">SEARCH FOR A ROOM</div>
<div class="tab tab-offer abs">OFFER A ROOM</div>
<form class="panel abs"></form>
<div class="tab-pointer abs"></div>

<span class="label abs" style="left:142px;top:265px">I'm a / We are</span>
<div class="check abs" style="left:201px;top:263px"><span class="box"></span>Male</div>
<div class="check abs" style="left:250px;top:263px"><span class="box"></span>Female</div>
<div class="check abs" style="left:313px;top:263px"><span class="box"></span>Couple</div>

<span class="label abs" style="left:144px;top:291px">Looking for Room</span>
<span class="label abs" style="left:280px;top:291px">City</span>
<span class="label abs" style="left:413px;top:291px">Size of room</span>
<span class="label abs" style="left:553px;top:291px">Bathroom</span>
<div class="select abs" style="left:143px;top:307px">Private<i class="chev"></i></div>
<div class="select abs" style="left:278px;top:307px">City or postal code</div>
<div class="select abs" style="left:414px;top:307px">Any<i class="chev"></i></div>
<div class="select abs" style="left:550px;top:307px">Shared<i class="chev"></i></div>

<span class="label abs" style="left:142px;top:346px">Bed size</span>
<span class="label abs" style="left:277px;top:346px">Type of housemates</span>
<span class="label abs" style="left:413px;top:346px">Parking</span>
<span class="label abs" style="left:551px;top:346px">Minimum contract</span>
<div class="select abs" style="left:141px;top:362px">Any<i class="chev"></i></div>
<div class="select abs" style="left:277px;top:362px">Shared<i class="chev"></i></div>
<div class="select abs" style="left:413px;top:362px">Street<i class="chev"></i></div>
<div class="select abs" style="left:549px;top:362px">3 Months<i class="chev"></i></div>

<span class="label abs" style="left:143px;top:402px">Internet speed</span>
<div class="select abs" style="left:141px;top:418px">50 mbps<i class="chev"></i></div>
<div class="check abs" style="left:277px;top:425px"><span class="box"></span>Smoking</div>
<div class="check abs" style="left:354px;top:425px"><span class="box"></span>Non-smoking</div>
<div class="submit abs">Submit</div>

<h2 class="section-title abs" style="left:118px;top:517px">Featured Available Rooms</h2>
<div class="city-pick abs">Marrowby<i class="chev"></i></div>

<div class="slide-btn abs" style="left:67px"><i style="transform:rotate(45deg);margin-left:4px"></i></div>
<div class="slide-btn abs" style="left:729px"><i style="transform:rotate(-135deg);margin-right:4px"></i></div>

<article class="room abs" style="left:118px">
  <div class="room-photo" role="img" aria-label="Bedroom with a grey upholstered bed, white linen and a patterned rug" style="background:linear-gradient(160deg,#d8d2c8,#b8a894 60%,#8c7a66)"></div>
  <div class="room-body">
    <h4>Adress</h4>
    <p class="room-addr">4096 N Fenwold St,&nbsp; Marrowby VA 32101, USA</p>
    <h4>Rental price</h4>
    <p class="room-price">$20.50/Month</p>
    <h4>Amenities</h4>
    <p class="room-desc">Lorem ipsum dolor sit amet, consectetur adipiscing elit. Proin rhoncus, erat fringilla viverra egestas, risus massa lacinia felis, eget faucibus est elit id enim.</p>
  </div>
  <div class="room-go abs" style="left:162px;top:264px"><i></i></div>
</article>

<article class="room abs" style="left:322px">
  <div class="room-photo" role="img" aria-label="Bedroom with a white wooden bed, blue patterned quilt and light blue walls" style="background:linear-gradient(160deg,#a9cbd6,#7fa4ae 55%,#c9c2b6)"></div>
  <div class="room-body">
    <h4>Adress</h4>
    <p class="room-addr">4096 N Fenwold St,&nbsp; Marrowby VA 32101, USA</p>
    <h4>Rental price</h4>
    <p class="room-price">$20.50/Month</p>
    <h4>Amenities</h4>
    <p class="room-desc">Lorem ipsum dolor sit amet, consectetur adipiscing elit. Proin rhoncus, erat fringilla viverra egestas, risus massa lacinia felis, eget faucibus est elit id enim.</p>
  </div>
  <div class="room-go abs" style="left:159px;top:264px"><i></i></div>
</article>

<article class="room abs" style="left:525px">
  <div class="room-photo" role="img" aria-label="Bright bedroom with a green headboard and floral white bedding" style="background:linear-gradient(160deg,#e6e6e2,#c8cbc4 55%,#9fa596)"></div>
  <div class="room-body">
    <h4>Adress</h4>
    <p class="room-addr">4096 N Fenwold St,&nbsp; Marrowby VA 32101, USA</p>
    <h4>Rental price</h4>
    <p class="room-price">$20.50/Month</p>
    <h4>Amenities</h4>
    <p class="room-desc">Lorem ipsum dolor sit amet, consectetur adipiscing elit. Proin rhoncus, erat fringilla viverra egestas, risus massa lacinia felis, eget faucibus est elit id enim.</p>
  </div>
  <div class="room-go abs" style="left:161px;top:264px"><i></i></div>
</article>

<section class="how abs"></section>
<h2 class="section-title abs" style="left:0;top:910px;width:822px;text-align:center">How it Works</h2>

<div class="step abs" style="left:115px">
  <div class="step-icon" role="img" aria-label="Illustration of a house with a magnifying glass" style="background:linear-gradient(135deg,#4f95d8,#e9b44a)"></div>
  <h3>Start your Serch</h3>
  <p>Proin rhoncus, erat fringilla viverra egestas, risus massa lacinia felis, eget faucibus est elit id enim.</p>
</div>
<div class="step abs" style="left:321px">
  <div class="step-icon" role="img" aria-label="Illustration of an upward arrow with a coin and a small house" style="background:linear-gradient(135deg,#4f95d8,#e9b44a)"></div>
  <h3>Upgrade to Premium</h3>
  <p>Proin rhoncus, erat fringilla viverra egestas, risus massa lacinia felis, eget faucibus est elit id enim.</p>
</div>
<div class="step abs" style="left:524px">
  <div class="step-icon" role="img" aria-label="Illustration of an open door" style="background:linear-gradient(135deg,#4f95d8,#e9b44a)"></div>
  <h3 style="margin-top:19px">Find a Room</h3>
  <p>Proin rhoncus, erat fringilla viverra egestas, risus massa lacinia felis, eget faucibus est elit id enim.</p>
</div>

<footer class="site-footer abs">
  <span class="foot-link abs" style="left:118px">PRIVACY POLICY</span>
  <span class="foot-link abs" style="left:183px">TERMS OF USE</span>
  <div class="social abs" style="left:663px">
    <span aria-label="Social link"></span><span aria-label="Social link"></span><span aria-label="Social link"></span>
  </div>
</footer>
<p class="copyright abs">copyright 2019 quellnest.com All Righrs Reserved.</p>

</body>
</html>
```